Design business card

Looking for a Business Card design.
Our company is an IT company
Business Card should contain :

LOGOS + SLOGAN+ NAME of the holder+ Job Title+Phone number+Email+Location
Background should be white

The business card should be Professional with attractive and unique look

You also Provide full statianry set together with business card
Thank you, and looking forward to see your creativity

```html
<!DOCTYPE html>
<html lang="en">
<head>
<meta charset="utf-8">
<title>Vexora business card</title>
<link href="https://fonts.googleapis.com/css2?family=Open+Sans:wght@400;600;700&display=swap" rel="stylesheet">
<style>
  :root {
    --page-bg: #e9ebee;
    --card-white: #ffffff;
    --card-blue-top: #1e8ee0;
    --card-blue-bottom: #2aa3e6;
    --ink-dark: #2c2f33;
    --ink-mid: #44484d;
    --accent-blue: #1f8ed8;
    --slogan-dark: #1b3f66;
    --card-shadow: rgba(20, 30, 45, 0.18);
  }
  * { box-sizing: border-box; margin: 0; padding: 0; }
  html, body {
    width: 1200px; height: 900px; overflow: hidden;
    background: var(--page-bg);
    font-family: "Open Sans", sans-serif;
  }
  .canvas {
    position: relative; width: 1200px; height: 900px;
  }
  .card {
    position: absolute; top: 170px;
    width: 340px; height: 560px;
    border-radius: 22px;
    box-shadow: 0 10px 30px var(--card-shadow);
    overflow: hidden;
  }
  .card--front {
    left: 220px;
    background: linear-gradient(160deg, var(--card-blue-top), var(--card-blue-bottom));
  }
  .card--back {
    left: 640px;
    background: var(--card-white);
  }
  .brand {
    display: flex; align-items: center; gap: 10px;
  }
  .brand__dot {
    width: 14px; height: 14px; border-radius: 50%;
  }
  .brand__name {
    font-weight: 400; font-size: 58px; letter-spacing: 1px; line-height: 1;
  }
  .slogan {
    font-weight: 700; font-size: 20px; margin-top: 4px;
  }
  /* front */
  .card--front .brand-block {
    position: absolute; left: 40px; top: 210px;
  }
  .card--front .brand__name { color: var(--ink-dark); }
  .card--front .brand__dot { background: var(--card-white); }
  .card--front .slogan { color: var(--slogan-dark); padding-left: 50px; }
  .card--front .website {
    position: absolute; right: 40px; bottom: 44px;
    font-size: 15px; color: var(--ink-dark);
  }
  /* back */
  .holder {
    position: absolute; left: 40px; top: 48px;
  }
  .holder__name { font-weight: 700; font-size: 22px; color: var(--ink-mid); }
  .holder__title { font-weight: 600; font-size: 13px; color: var(--ink-mid); margin-top: 2px; }
  .card--back .brand-block {
    position: absolute; left: 40px; top: 150px;
  }
  .card--back .brand__name { color: var(--ink-dark); font-size: 52px; }
  .card--back .brand__dot { background: var(--accent-blue); }
  .card--back .slogan { color: var(--accent-blue); font-size: 17px; padding-left: 44px; }
  .contact {
    position: absolute; left: 70px; top: 300px;
    font-size: 15px; color: var(--ink-mid); line-height: 1.45;
    list-style: none;
  }
  .contact__group + .contact__group { margin-top: 18px; }
</style>
</head>
<body>
<main class="canvas">
  <section class="card card--front" aria-label="Card front">
    <div class="brand-block">
      <div class="brand">
        <span class="brand__dot"></span>
        <span class="brand__name">Vexora</span>
      </div>
      <p class="slogan">Sologan Here</p>
    </div>
    <p class="website">www.vexora-it.com</p>
  </section>

  <section class="card card--back" aria-label="Card back">
    <div class="holder">
      <p class="holder__name">Daniel Reeve</p>
      <p class="holder__title">Founder &amp; CEO</p>
    </div>
    <div class="brand-block">
      <div class="brand">
        <span class="brand__dot"></span>
        <span class="brand__name">Vexora</span>
      </div>
      <p class="slogan">Sologan Here</p>
    </div>
    <div class="contact">
      <div class="contact__group">
        <p>004 210 55 31</p>
        <p>004 210 55 32</p>
      </div>
      <div class="contact__group">
        <p>hello@vexora-it.com</p>
        <p>www.vexora-it.com</p>
      </div>
      <div class="contact__group">
        <p>Talackerweg 18</p>
        <p>8047 Zürich</p>
      </div>
    </div>
  </section>
</main>
</body>
</html>
```